Email Signiture and letterhead design

we are looking for a modern business design to incorporate our logo and qel certification plus social icons for Vorlant, Pelmora, and zandoro
they must include our UK vat and also company registration as text but I can fill these out. Email signature to have a link/icon to our webshop www.trexolan.co.uk

Target Market(s)

All

Font styles to use
Serif
Sans Serif

Requirements
Must have
• Address, tel, email , web details incorperated
Nice to have
• a professional looking letter head and email signiture, Email signature to have a link/icon to our webshop www.trexolan.co.uk

```html
<!DOCTYPE html>
<html lang="en">
<head>
<meta charset="utf-8">
<title>Trexolan Hubs Ltd — Letterhead and Email Signature</title>
<link href="https://fonts.googleapis.com/css2?family=Roboto:wght@400;500&family=Open+Sans:wght@400;600;700&display=swap" rel="stylesheet">
<style>
  :root {
    --board: #8a8a8a;
    --paper: #f6f4f4;
    --ink: #3a3a3a;
    --ink-soft: #555555;
    --red: #ec1c24;
    --label: #ffffff;
  }
  * { margin: 0; padding: 0; box-sizing: border-box; }
  html, body { width: 1200px; height: 873px; overflow: hidden; }
  body {
    background: var(--board);
    position: relative;
    font-family: "Open Sans", sans-serif;
    color: var(--ink);
  }
  .sheet {
    position: absolute;
    background: var(--paper);
    box-shadow: 0 2px 6px rgba(0,0,0,0.25);
    overflow: hidden;
  }
  .letterhead { left: 51px; top: 70px; width: 524px; height: 738px; }
  .signature-card { left: 644px; top: 351px; width: 486px; height: 137px; }
  .sheet-label {
    position: absolute;
    color: var(--label);
    font-family: "Roboto", sans-serif;
    font-size: 13px;
    transform: translateX(-50%);
  }
  .social { position: absolute; display: flex; gap: 4px; }
  .social span {
    width: 15px; height: 15px; border-radius: 50%;
    background: var(--red); display: block;
  }
  .brand {
    position: absolute;
    display: flex; align-items: center; gap: 6px;
    font-family: "Open Sans", sans-serif;
    font-weight: 600;
    color: var(--ink);
    letter-spacing: 0.3px;
    white-space: nowrap;
  }
  .brand .mark { border-radius: 50%; background: var(--red); display: block; }
  .contact { position: absolute; font-size: 9.5px; line-height: 12.7px; color: var(--ink-soft); white-space: nowrap; }
  .contact .phone { display: flex; align-items: center; gap: 5px; margin-bottom: 6px; }
  .greeting {
    position: absolute; left: 39px; top: 207px;
    font-family: "Roboto", sans-serif; font-size: 14.5px; line-height: 18px; color: var(--ink);
  }
  .letter-body {
    position: absolute; left: 39px; top: 251px; width: 438px;
    font-family: "Roboto", sans-serif; font-size: 8.3px; line-height: 12.6px;
    color: var(--ink-soft); text-align: justify;
  }
  .letter-body p { margin-bottom: 12.6px; }
  .closing { position: absolute; left: 39px; top: 516px; font-family: "Roboto", sans-serif; font-size: 8px; line-height: 10px; color: var(--ink-soft); }
  .sign-mark { position: absolute; left: 49px; top: 551px; width: 68px; height: 26px; background: linear-gradient(90deg, rgba(30,30,50,0.10), rgba(30,30,50,0.04)); }
  .signer { position: absolute; left: 55px; top: 609px; font-family: "Roboto", sans-serif; }
  .signer .name { font-size: 11.5px; line-height: 14px; color: var(--ink); }
  .signer .role { font-size: 8.5px; line-height: 11px; color: var(--ink-soft); margin-top: 2px; }
  .web { position: absolute; font-size: 8.5px; line-height: 11px; font-weight: 700; letter-spacing: 1.2px; color: var(--ink); white-space: nowrap; }
  .web .accent { color: var(--red); }
  .stripe { position: absolute; height: 3px; background: var(--red); right: 0; }
</style>
</head>
<body>

  <section class="sheet letterhead" aria-label="Letterhead">
    <div class="social" style="left:456px; top:14px;"><span></span><span></span><span></span></div>

    <div class="brand" style="left:39px; top:112px; font-size:13px;">
      <span class="mark" style="width:12px; height:12px;"></span>Trexolan Hubs Ltd
    </div>

    <div class="contact" style="left:370px; top:63px;">
      <div class="phone">
        <svg width="9" height="9" viewBox="0 0 24 24"><path fill="#ec1c24" d="M6.6 10.8a15 15 0 0 0 6.6 6.6l2.2-2.2a1 1 0 0 1 1-.25 11.4 11.4 0 0 0 3.6.57 1 1 0 0 1 1 1V20a1 1 0 0 1-1 1A17 17 0 0 1 3 4a1 1 0 0 1 1-1h3.5a1 1 0 0 1 1 1 11.4 11.4 0 0 0 .57 3.6 1 1 0 0 1-.25 1z"/></svg>
        +44 (0) 161 496 0712
      </div>
      VAT - ABC-1A2345<br>
      Kestrel Row North,<br>
      Dunmere,<br>
      Halbury, HB4 7QT
    </div>

    <div class="greeting">Dear Mr. Corwell,</div>

    <div class="letter-body">
      <p>Lorem ipsum dolor sit amet, consectetur adipiscing elit. Donec orci purus, luctus vitae dignissim eu, iaculis sed purus. Vivamus faucibus, ipsum nec aliquet viverra, leo mauris condimentum ligula, sit amet sagittis enim ligula quis arcu. Nam egestas tortor id nisi porttitor mattis. In tortor ante, ultricies in suscipit a, tempus non massa. Vivamus et auctor mi. Fusce vel massa nulla. Phasellus nec eros mauris, et scelerisque orci.</p>
      <p>Donec malesuada orci vitae nulla accumsan porta a id massa. Quisque accumsan iaculis magna sit amet fringilla. Maecenas consequat, magna eget tincidunt semper, odio nibh rutrum mi, id feugiat ante nisi eu risus. Vestibulum nunc orci, rhoncus a placerat in, ultricies in mi. Cras mattis varius eros, vel fringilla nisi suscipit eget. Quisque scelerisque sagittis nulla at porttitor.</p>
      <p>Sed id augue vitae urna euismod commodo aliquet a quam. Pellentesque arcu velit, cursus et malesuada ut, consequat et diam. Nullam erat sem, rhoncus id ullamcorper vitae, rhoncus et arcu. In ultricies ultricies nulla, ut rutrum nisi iaculis at. Donec eu magna a metus ornare faucibus. Fusce aliquet faucibus ultricies. Morbi semper, est id tincidunt gravida, sem arcu adipiscing lacus, ac bibendum nulla leo eu purus. Quisque nec diam sed risus consectetur a ccumsan quis quis nibh. Vestibulum id purus lorem.</p>
      <p>It is a long established fact that a reader will be distracted by the readable content of a page when looking at its layout. The point of using Lorem Ipsum is that it has a more-or-less normal distribution of letters, as opposed to using 'Content here, content here', making it look like readable English. Many desktop publishing packages</p>
    </div>

    <div class="closing">Sincerely,</div>
    <div class="sign-mark" role="img" aria-label="Handwritten signature"></div>
    <div class="signer">
      <div class="name">Alden Rhys</div>
      <div class="role">CEO/ Founder</div>
    </div>

    <div class="web" style="left:39px; top:709px;">www.<span class="accent">trexolan</span>.co.uk</div>
    <div class="stripe" style="left:376px; top:693px;"></div>
    <div class="stripe" style="left:251px; top:703px;"></div>
    <div class="stripe" style="left:210px; top:713px;"></div>
  </section>
  <div class="sheet-label" style="left:277px; top:824px;">Letterhead_01</div>

  <section class="sheet signature-card" aria-label="Email signature">
    <div class="social" style="left:416px; top:16px;"><span></span><span></span><span></span></div>

    <div class="brand" style="left:31px; top:51px; font-size:10.5px;">
      <span class="mark" style="width:10px; height:10px;"></span>Trexolan Hubs Ltd
    </div>

    <div class="contact" style="left:31px; top:80px; font-size:9.5px;">
      <div style="font-weight:700; color:var(--ink); margin-bottom:4px;">+44 (0) 161 496 0712</div>
      VAT - ABC-1A2345<br>
      Kestrel Row North, Dunmere, Halbury, HB4 7QT
    </div>

    <div class="web" style="right:15px; top:81px;">www.trexolan.co.uk</div>
    <div class="stripe" style="left:417px; top:100px;"></div>
    <div class="stripe" style="left:359px; top:111px;"></div>
    <div class="stripe" style="left:340px; top:121px;"></div>
  </section>
  <div class="sheet-label" style="left:886px; top:510px;">Email Signature</div>

</body>
</html>
```